Brightway Inc. Business Card Design

Brightway Inc. is in search of a great clean design for our business cards!

Looking to incorporate our full logo and watermark on side one (however, I am open to having the text and watermark separated within the design.)

On side two, I am looking to have contact information (Name, Position, Phone #, Email, Website (www.thebrightway.ca). Can have the logo and/or watermark as part of the design if applicable.

Please add tagline "Where Shine Counts" on either side 1 or 2. This tagline can be in a sans serif, serif or cursive font as long as it compliments overall design. Capitalization can be title or sentence case depending on how it fits within the design.

Get creative!! Looking for a clean, crisp, premium design! Looking for a glossy card finish with spot UV features when printed. Cards will also be printed with rounded corners. Standard dimensions (3.5 x 2).

Target Market(s)

B2B - primary clients are business owners or property management corporations. (residential jobs are few and far between)

Industry/Entity Type

Business

Contact Information for Business Card

- clean, crisp design
- double sided
- spot UV accents and glossy finish upon printing
- standard business card size (3.5 x 2) with rounded corners
- please see project description for requirements per side

Font styles to use
Sans Serif

Requirements
Must have
• - adequate bleeds with print ready files
• - cohesive design elements between side 1 & 2
• - spot UV elements (can be on both sides or just one, use your discretion)
• - colour pallet should match the logo file provided
• - incorporate tagline "where shine counts" (this tagline can be in a serif or sans serif font as long as it is complimentary to the overall design.
Nice to have
• - Premium elements with a clean design
Should not have
• - Please omit cartoon or whimsical like designs, think premium.
• - Colours should not stray from the pallet of the provided logo.

```html
<!DOCTYPE html>
<html lang="en">
<head>
<meta charset="utf-8">
<title>Brightway Inc. Business Card</title>
<link rel="stylesheet" href="https://fonts.googleapis.com/css2?family=Montserrat:wght@300;400;500;800&display=swap">
<style>
  :root {
    --navy: #22284b;
    --teal: #2db3b8;
    --white: #ffffff;
    --backdrop: #e9e9ec;
  }
  * { box-sizing: border-box; margin: 0; padding: 0; }
  html, body { width: 1200px; height: 750px; overflow: hidden; }
  body {
    background: var(--backdrop);
    font-family: "Montserrat", sans-serif;
    position: relative;
  }
  .card {
    position: absolute;
    top: 232px;
    width: 500px;
    height: 286px;
    border-radius: 22px;
    overflow: hidden;
    box-shadow: 0 10px 24px rgba(0,0,0,0.18);
  }
  .card--front { left: 70px; background: var(--navy); }
  .card--back { left: 630px; background: var(--teal); }

  .front__band {
    position: absolute;
    left: 0; right: 0;
    top: 58px; height: 170px;
    background: var(--teal);
    display: flex;
    flex-direction: column;
    align-items: center;
    justify-content: center;
  }
  .brand {
    display: flex;
    align-items: center;
    gap: 8px;
    color: var(--white);
    font-weight: 800;
    text-transform: uppercase;
    letter-spacing: -0.5px;
    white-space: nowrap;
  }
  .brand__mark {
    background: var(--white);
    flex: none;
  }
  .brand--front { font-size: 36px; }
  .brand--front .brand__mark { width: 30px; height: 30px; }
  .tagline {
    margin-top: 10px;
    color: var(--navy);
    font-size: 11px;
    font-weight: 500;
    letter-spacing: 3.5px;
    text-transform: uppercase;
    white-space: nowrap;
  }
  .brand--back {
    position: absolute;
    left: 22px; bottom: 24px;
    font-size: 24px;
  }
  .brand--back .brand__mark { width: 21px; height: 21px; }

  .back__panel {
    position: absolute;
    top: 0; bottom: 0;
    right: 10px;
    width: 178px;
    background: var(--navy);
    color: var(--white);
    text-align: right;
    padding: 18px 14px 22px 10px;
    display: flex;
    flex-direction: column;
    font-size: 8.5px;
    font-weight: 400;
    letter-spacing: 0.4px;
    text-transform: uppercase;
    line-height: 1.45;
  }
  .back__edge {
    position: absolute;
    top: 0; bottom: 0; right: 0;
    width: 10px;
    background: var(--teal);
  }
  .contact__item + .contact__item { margin-top: 14px; }
  .person { margin-top: auto; }
  .person__name {
    font-size: 15px;
    font-weight: 300;
    letter-spacing: 0.3px;
    line-height: 1.1;
    white-space: nowrap;
  }
  .person__role {
    color: var(--teal);
    font-size: 8px;
    margin-top: 3px;
  }
</style>
</head>
<body>
  <section class="card card--front" aria-label="Card front">
    <div class="front__band">
      <div class="brand brand--front">
        <span class="brand__mark"></span>
        <span class="brand__name">Brightway Inc.</span>
      </div>
      <p class="tagline">Where Shine Counts</p>
    </div>
  </section>

  <section class="card card--back" aria-label="Card back">
    <div class="brand brand--back">
      <span class="brand__mark"></span>
      <span class="brand__name">Brightway Inc.</span>
    </div>
    <div class="back__panel">
      <p class="contact__item">480 Harbour Ave<br>Vale, BC 10245</p>
      <p class="contact__item">(604) 555-0142<br>hello@thebrightway.ca</p>
      <p class="contact__item">www.thebrightway.ca</p>
      <div class="person">
        <p class="person__name">DANA WHITLOW</p>
        <p class="person__role">Project Director</p>
      </div>
    </div>
    <div class="back__edge"></div>
  </section>
</body>
</html>
```